Business Card Design Project

Hello Designers, hope you are all aiming enjoy the weekend
I have the Business Logo (uploaded), you can alter the color which ever way you think would work,
Im looking for a simple yet striking feel, something which will stay memorable (I have uploaded 3 examples for you to flick through)
Information on the card, will just be the bare minimum,
Double Sided
Info being
i.e.
Name
Number
Website
ABN
Teo Marlowick
+482710365 (singapore)
+615093284 (Australia)
+790428153 (America)
www.lumoren-match.example
ABN 90817263
Enjoy,
Teo

```html
<!DOCTYPE html>
<html lang="en">
<head>
<meta charset="utf-8">
<title>Lumoren Match – Business Card</title>
<link rel="stylesheet" href="https://fonts.googleapis.com/css2?family=Arimo:wght@700&family=Poppins:wght@500&display=swap">
<style>
  :root {
    --canvas: #e5eef0;
    --frame-pink: #e8308a;
    --card-white: #ffffff;
    --brand-red: #c8143c;
    --text-pink: #e8308a;
  }
  * { margin: 0; padding: 0; box-sizing: border-box; }
  html, body {
    width: 1200px; height: 900px; overflow: hidden;
    background: var(--canvas);
  }
  .canvas { position: relative; width: 1200px; height: 900px; }

  .card {
    position: absolute;
    background: var(--frame-pink);
    border-radius: 16px;
    box-shadow: 0 2px 6px rgba(0,0,0,0.18);
  }
  .card-inner {
    position: absolute;
    inset: 22px;
    background: var(--card-white);
    overflow: hidden;
  }
  .card-front { left: 33px; top: 10px; width: 667px; height: 425px; }
  .card-back  { left: 508px; top: 455px; width: 667px; height: 425px; }

  .brand-mark {
    position: absolute;
    background: var(--brand-red);
    border-radius: 18px;
  }
  .brand-name {
    position: absolute;
    font-family: "Poppins", sans-serif;
    font-weight: 500;
    color: var(--brand-red);
    white-space: nowrap;
    text-align: center;
    letter-spacing: 0.5px;
  }

  .card-front .brand-mark { left: 241px; top: 65px; width: 145px; height: 145px; }
  .card-front .brand-name { left: 0; right: 0; top: 238px; font-size: 52px; line-height: 70px; }

  .card-back .brand-mark { left: 88px; top: 100px; width: 144px; height: 144px; border-radius: 16px; }
  .card-back .brand-name { left: 18px; width: 284px; top: 256px; font-size: 34px; line-height: 46px; }

  .divider {
    position: absolute;
    left: 311px; top: 100px; width: 4px; height: 165px;
    background: linear-gradient(to bottom, rgba(232,48,138,0), var(--frame-pink) 45%, rgba(232,48,138,0));
  }

  .name-tab {
    position: absolute;
    left: 332px; top: 35px; width: 291px; height: 80px;
    background: var(--frame-pink);
    border-radius: 14px 0 0 14px;
    font-family: "Arimo", sans-serif;
    font-weight: 700;
    font-size: 35px;
    color: var(--card-white);
    line-height: 80px;
    padding-left: 16px;
    white-space: nowrap;
  }

  .contact-list {
    position: absolute;
    left: 357px; top: 130px;
    list-style: none;
    font-family: "Arimo", sans-serif;
    font-weight: 700;
    font-size: 18px;
    letter-spacing: -0.2px;
    line-height: 25.5px;
    color: var(--text-pink);
    white-space: nowrap;
  }
</style>
</head>
<body>
<main class="canvas">
  <section class="card card-front" aria-label="Card front">
    <div class="card-inner">
      <div class="brand-mark" aria-hidden="true"></div>
      <div class="brand-name">Lumoren Match</div>
    </div>
  </section>

  <section class="card card-back" aria-label="Card back">
    <div class="card-inner">
      <div class="brand-mark" aria-hidden="true"></div>
      <div class="brand-name">Lumoren Match</div>
      <div class="divider" aria-hidden="true"></div>
      <div class="name-tab">Teo Marlowick</div>
      <ul class="contact-list">
        <li>+482710365 (singapore)</li>
        <li>+615093284 (Australia)</li>
        <li>+790428153 (America)</li>
        <li>www.lumoren-match.example</li>
        <li>ABN 90817263</li>
      </ul>
    </div>
  </section>
</main>
</body>
</html>
```